Modern Business Card

Modern professional business card with more than just logo and demographic info. Something memorable.

We are a trendy/modern chiropractic group with an emphasis on neurology, hence the minimalist-type brain logo. We want to convey that modern and technical aspect with professionalism and the elite nature of our practice environment.

```html
<!DOCTYPE html>
<html lang="en">
<head>
<meta charset="utf-8">
<title>Keystone Spine – Business Card</title>
<link rel="stylesheet" href="https://fonts.googleapis.com/css2?family=Open+Sans:wght@400;600;700&display=swap">
<style>
  :root {
    --bg: #a9abad;
    --card: #f1f1f1;
    --blue: #4a7cb8;
    --ink: #1e1e1e;
    --line: #2a2a2a;
  }
  * { margin: 0; padding: 0; box-sizing: border-box; }
  html, body { width: 1200px; height: 929px; overflow: hidden; }
  body {
    background: var(--bg);
    font-family: "Open Sans", sans-serif;
    color: var(--ink);
    position: relative;
  }
  .card {
    position: absolute;
    top: 316px;
    width: 520px;
    height: 297px;
    background: var(--card);
    border-radius: 14px;
    overflow: hidden;
  }
  .card--front { left: 40px; }
  .card--back { left: 640px; }

  /* Front */
  .front__band {
    position: absolute; left: 0; right: 0; top: 88px; height: 118px;
    background: var(--blue);
    display: flex; align-items: center; justify-content: center; gap: 14px;
  }
  .brand-mark { width: 22px; height: 22px; background: var(--card); border-radius: 3px; }
  .brand-name {
    color: var(--card); font-weight: 600; font-size: 34px;
    letter-spacing: 3px; text-transform: uppercase;
  }
  .front__rule {
    position: absolute; left: 18px; right: 18px; bottom: 18px;
    height: 1px; background: var(--blue);
  }
  .front__web {
    position: absolute; bottom: 24px; left: 0; right: 0;
    text-align: center; color: var(--blue); font-size: 13px; letter-spacing: 1px;
  }

  /* Back */
  .back__logo {
    position: absolute; right: 26px; top: 34px;
    display: flex; align-items: center; gap: 8px;
  }
  .back__logo .brand-mark { width: 14px; height: 14px; background: var(--blue); }
  .back__logo .brand-name { color: var(--ink); font-size: 20px; letter-spacing: 2px; }
  .person { position: absolute; left: 34px; top: 36px; }
  .person__name { font-size: 27px; line-height: 1.05; letter-spacing: 0.5px; text-transform: uppercase; }
  .person__name strong { font-weight: 700; }
  .person__name span { font-weight: 400; }
  .person__title { font-size: 14px; letter-spacing: 1px; text-transform: uppercase; }
  .accent-bar { position: absolute; left: 0; top: 48px; width: 22px; height: 6px; background: var(--blue); }
  .name-rule { position: absolute; left: 34px; top: 104px; width: 150px; height: 4px; background: var(--blue); }
  .divider { position: absolute; left: 184px; right: 26px; top: 105px; height: 1px; background: var(--line); }
  .contacts { position: absolute; left: 34px; top: 140px; list-style: none; }
  .contacts li, .address { display: flex; align-items: center; gap: 14px; font-size: 14px; margin-bottom: 16px; }
  .icon {
    width: 22px; height: 22px; border-radius: 3px; background: var(--blue);
    display: flex; align-items: center; justify-content: center; flex: none;
  }
  .address { position: absolute; left: 290px; top: 140px; align-items: flex-start; line-height: 1.45; }
  .back__edge { position: absolute; left: 0; right: 0; bottom: 0; height: 8px; background: var(--blue); }
</style>
</head>
<body>
  <section class="card card--front">
    <div class="front__band">
      <span class="brand-mark"></span>
      <span class="brand-name">Keystone Spine</span>
    </div>
    <p class="front__web">www.domainname.com</p>
    <div class="front__rule"></div>
  </section>

  <section class="card card--back">
    <div class="accent-bar"></div>
    <div class="person">
      <p class="person__name"><strong>Daniel</strong> <span>Reyes</span></p>
      <p class="person__title">Founder &amp; CEO</p>
    </div>
    <div class="back__logo">
      <span class="brand-mark"></span>
      <span class="brand-name">Keystone Spine</span>
    </div>
    <div class="name-rule"></div>
    <div class="divider"></div>
    <ul class="contacts">
      <li>
        <span class="icon"><svg width="12" height="12" viewBox="0 0 12 12"><rect x="3" y="1" width="6" height="10" rx="1" fill="none" stroke="#fff" stroke-width="1.2"/></svg></span>
        012-345-6789
      </li>
      <li>
        <span class="icon"><svg width="12" height="12" viewBox="0 0 12 12" fill="none" stroke="#fff" stroke-width="1.1"><path d="M1.5 5a6 6 0 0 1 9 0M3.2 7a3.5 3.5 0 0 1 5.6 0"/><circle cx="6" cy="9.3" r="0.9" fill="#fff" stroke="none"/></svg></span>
        www.domainname.com
      </li>
    </ul>
    <div class="address">
      <span class="icon"><svg width="12" height="12" viewBox="0 0 12 12"><path d="M6 11s-3.5-4-3.5-6.3a3.5 3.5 0 0 1 7 0C9.5 7 6 11 6 11z" fill="#fff"/><circle cx="6" cy="4.7" r="1.2" fill="#4a7cb8"/></svg></span>
      <span>Address, Suit, Floor<br>City, Country, Zipcode</span>
    </div>
    <div class="back__edge"></div>
  </section>
</body>
</html>
```